Copper Kettle Catering
Business Cards and Letterhead
Copper Kettle Catering -
Creative Brief
Use standard fonts
R Danela Forsythe
Chef/Owner
287 W 93rd St FL2 New York, NY 10025
copperkettlecatering@mailbox.example
copperkettlecatering.example

```html
<!DOCTYPE html>
<html lang="en">
<head>
<meta charset="utf-8">
<title>Copper Kettle Catering – Business Card</title>
<link rel="stylesheet" href="https://fonts.googleapis.com/css2?family=Arimo:wght@400;700&display=swap">
<style>
  :root {
    --stage: #ebe7e2;
    --card-front: #ffffff;
    --card-back-light: #f6f6f6;
    --card-back-dark: #dcdcdc;
    --ink: #1a1a1a;
    --band: #111111;
    --band-soft: #b9b9b9;
    --brand: #8a5a1e;
  }
  html, body {
    margin: 0;
    width: 1200px;
    height: 367px;
    overflow: hidden;
    background: var(--stage);
    font-family: "Arimo", Arial, sans-serif;
    color: var(--ink);
  }
  .canvas { position: relative; width: 1200px; height: 367px; }
  .card {
    position: absolute;
    top: 31px;
    width: 545px;
    height: 305px;
    border-radius: 22px;
    overflow: hidden;
    box-shadow: 0 2px 6px rgba(0,0,0,.25);
  }
  .card--front { left: 19px; background: var(--card-front); }
  .card--back {
    left: 617px;
    background: radial-gradient(ellipse at 50% 45%, var(--card-back-light) 0%, var(--card-back-dark) 100%);
  }
  .brand-name {
    position: absolute;
    margin: 0;
    font-weight: 700;
    color: var(--brand);
    white-space: nowrap;
  }
  .card--front .brand-name { left: 22px; width: 270px; top: 104px; text-align: center; font-size: 22px; }
  .card--back .brand-name { left: 0; right: 0; top: 118px; text-align: center; font-size: 34px; }
  .contact {
    position: absolute;
    left: 300px;
    top: 46px;
    font-size: 11px;
    line-height: 1.5;
    white-space: nowrap;
  }
  .contact p { margin: 0; }
  .contact .name { font-size: 14px; }
  .contact .title { margin-bottom: 16px; }
  .contact .address { margin-bottom: 28px; }
  .band { position: absolute; left: 0; bottom: 0; }
  .website { position: absolute; font-size: 11px; white-space: nowrap; }
  .card--front .website { right: 18px; top: 272px; }
  .card--back .website { left: 0; right: 0; top: 272px; text-align: center; }
</style>
</head>
<body>
<div class="canvas">
  <section class="card card--front">
    <p class="brand-name">Copper Kettle Catering</p>
    <div class="contact">
      <p class="name">R Danela Forsythe</p>
      <p class="title">Chef/Owner</p>
      <p class="address">287 W 93rd St FL2<br>New York, NY 10025</p>
      <p>P : 555.014.2738</p>
      <p>F : 555.019.4406</p>
      <p>E : copperkettlecatering@mailbox.example</p>
    </div>
    <svg class="band" width="545" height="60" viewBox="0 0 545 60" aria-hidden="true">
      <path d="M0 24 C120 18 240 14 545 10 L545 14 C260 20 140 26 0 34 Z" fill="var(--band-soft)"/>
      <path d="M0 30 C110 24 240 22 330 26 C300 36 290 52 300 60 L0 60 Z" fill="var(--band)"/>
    </svg>
    <div class="website">www.copperkettlecatering.example</div>
  </section>

  <section class="card card--back">
    <p class="brand-name">Copper Kettle Catering</p>
    <div class="website">www.copperkettlecatering.example</div>
  </section>
</div>
</body>
</html>
```